need eczema bath soak label/bag

need you to recreate this please. ai file. recreate this exact image please. ...if you want a big tip, create some different styles.

Colors
0054AA
0677BA
7BADD7
CADEEF
E8F1F8

```html
<!DOCTYPE html>
<html lang="en">
<head>
<meta charset="utf-8">
<title>The Ocean Healed My A Bag – Bath Soak Label</title>
<link href="https://fonts.googleapis.com/css2?family=Montserrat:wght@600;700;800&display=swap" rel="stylesheet">
<style>
  :root {
    --blue-deep: #0054AA;
    --blue-mid: #0677BA;
    --blue-soft: #7BADD7;
    --blue-pale: #CADEEF;
    --blue-mist: #E8F1F8;
    --ink: #1E2A3B;
    --foam: #F3F6F8;
    --sea-teal: #4FC0B0;
    --sea-light: #8FD3C6;
    --sand: #F2B590;
    --sand-light: #F8DCCB;
  }
  * { box-sizing: border-box; margin: 0; padding: 0; }
  html, body {
    width: 1200px;
    height: 800px;
    overflow: hidden;
  }
  body {
    background: var(--blue-pale);
    font-family: "Montserrat", Arial, sans-serif;
    color: var(--ink);
    position: relative;
  }
  .label {
    position: absolute;
    left: 370px;
    top: 40px;
    width: 460px;
    height: 720px;
    overflow: hidden;
  }
  .label__photo {
    position: absolute;
    inset: 0;
    width: 100%;
    height: 100%;
  }
  .label__content {
    position: absolute;
    inset: 0;
    display: flex;
    flex-direction: column;
    align-items: center;
    text-align: center;
  }
  .title {
    margin-top: 190px;
    font-weight: 800;
    font-size: 50px;
    line-height: 1.06;
    letter-spacing: 1px;
    text-transform: uppercase;
  }
  .title__small { font-size: 34px; display: block; }
  .blurb {
    margin-top: 16px;
    width: 240px;
    font-weight: 700;
    font-size: 8.5px;
    line-height: 1.7;
    text-transform: uppercase;
    letter-spacing: 0.3px;
  }
  .range {
    margin-top: 22px;
    font-weight: 700;
    font-size: 13px;
    letter-spacing: 0.5px;
  }
  .batch {
    margin-top: 10px;
    font-weight: 800;
    font-size: 16px;
  }
  .brand {
    margin-top: 50px;
    display: flex;
    flex-direction: column;
    align-items: center;
    gap: 12px;
  }
  .brand__mark {
    width: 44px;
    height: 44px;
    background: var(--ink);
  }
  .brand__name {
    font-weight: 800;
    font-size: 20px;
    letter-spacing: 4px;
    text-transform: uppercase;
  }
</style>
</head>
<body>
  <main class="label">
    <svg class="label__photo" viewBox="0 0 460 720" preserveAspectRatio="none" role="img" aria-label="Aerial photograph of a turquoise wave breaking onto a sandy beach">
      <defs>
        <linearGradient id="shore" x1="0" y1="0" x2="0" y2="1">
          <stop offset="0" stop-color="#F3F6F8"/>
          <stop offset="0.12" stop-color="#F3F6F8"/>
          <stop offset="0.24" stop-color="#4FC0B0"/>
          <stop offset="0.44" stop-color="#4FC0B0"/>
          <stop offset="0.56" stop-color="#8FD3C6"/>
          <stop offset="0.64" stop-color="#F2B590"/>
          <stop offset="1" stop-color="#F8DCCB"/>
        </linearGradient>
      </defs>
      <rect width="460" height="720" fill="url(#shore)"/>
    </svg>

    <div class="label__content">
      <h1 class="title">
        <span class="title__small">The</span>
        Ocean<br>Healed<br>My A Bag
      </h1>
      <p class="blurb">Mineral ocean salts blended with oat and calm botanicals for a gentle, soothing soak.</p>
      <p class="range">OCEAN I&nbsp;&nbsp;IN A BA</p>
      <p class="batch">B 77 6. : 119</p>

      <div class="brand">
        <span class="brand__mark"></span>
        <span class="brand__name">Tidewell</span>
      </div>
    </div>
  </main>
</body>
</html>
```